Nightclub-type Event Poster Advertisement

Lumora Events is based in Christchurch, New Zealand and we have our next party coming up. We like a different flair for each of our events so are looking for some help from you guys. We are very flexible with everything - colours, layout, backgrounds, fonts, etc so it's ALL up to you. Attached is our company logo and the flyer (and poster) we used for our last party. Our website is lumoranz.example where you can find and use our photos and find more info about us if you desire.
Designs we are wanting: An A3 poster,an A6 flyer (smaller version of the poster is probably fine), tickets (140x68 mm). It would be great if a 5 mm bleed was included so we could get them printed directly.
Details for the event to be advertised are as followed:
Party Name: (TBD... will update ASAP)
05/07/2014
10pm-close
Lineup: 'Bazzo (Akl)', 'DJ Glimtrax', 'DJ's Morquent & Pelnavo', 'Quiet Harbour Pulse'.
Dorrin Hattles Central, Corner Fenwick & Oberly Streets
$10 Tickets
R18
Tickets & Enquiries: Marta on 0219047362
Presented by Lumora Entertainment
Thanks to everyone who reads this and please give it a go! Any questions don't hesitate to ask.
Target Market(s)
New Zealand Europeans in Christchurch, New Zealand between 18 and 25 years old.
Industry/Entity Type
Events
Look and feel

```html
<!DOCTYPE html>
<html lang="en">
<head>
<meta charset="utf-8">
<title>TBD — Lumora Entertainment</title>
<link rel="stylesheet" href="https://fonts.googleapis.com/css2?family=Comfortaa:wght@400;500&family=Pathway+Gothic+One&display=swap">
<style>
  :root {
    --bg-deep: #2a0b5c;
    --bg-mid: #5b1a8e;
    --bg-glow: #8a3cc0;
    --ink: #ffffff;
    --title-pink: #f6b3ee;
  }
  * { margin: 0; padding: 0; box-sizing: border-box; }
  html, body { width: 800px; height: 1200px; overflow: hidden; background: var(--bg-deep); }
  .poster {
    position: relative;
    width: 800px;
    height: 1200px;
    overflow: hidden;
    color: var(--ink);
    font-family: "Pathway Gothic One", sans-serif;
  }
  .backdrop {
    position: absolute;
    inset: 0;
    background:
      radial-gradient(ellipse 55% 40% at 35% 55%, rgba(74, 95, 208, 0.45), transparent 70%),
      radial-gradient(ellipse 50% 35% at 80% 20%, rgba(190, 90, 220, 0.55), transparent 70%),
      radial-gradient(ellipse 45% 35% at 20% 15%, rgba(160, 70, 210, 0.45), transparent 70%),
      radial-gradient(ellipse 60% 40% at 70% 85%, rgba(120, 50, 190, 0.5), transparent 70%),
      linear-gradient(160deg, var(--bg-mid) 0%, var(--bg-glow) 35%, var(--bg-deep) 70%, var(--bg-mid) 100%);
  }
  .presenter {
    position: absolute;
    top: 66px;
    width: 100%;
    text-align: center;
    font-family: "Comfortaa", sans-serif;
  }
  .presenter-name { font-size: 38px; font-weight: 400; letter-spacing: 1px; line-height: 1; }
  .presenter-verb { font-size: 21px; line-height: 1.2; }
  .event-date {
    position: absolute;
    top: 166px;
    width: 100%;
    text-align: center;
    font-family: "Comfortaa", sans-serif;
    font-size: 60px;
    font-weight: 400;
    letter-spacing: 1px;
  }
  .lineup {
    position: absolute;
    top: 240px;
    width: 100%;
    font-size: 40px;
    line-height: 54px;
  }
  .lineup-row { display: flex; justify-content: center; gap: 42px; }
  .party-name {
    position: absolute;
    top: 528px;
    width: 100%;
    text-align: center;
    font-family: "Pathway Gothic One", sans-serif;
    font-weight: 400;
    font-size: 180px;
    line-height: 1;
    letter-spacing: 24px;
    text-indent: 24px;
    color: var(--title-pink);
  }
  .venue {
    position: absolute;
    top: 890px;
    width: 100%;
    display: flex;
    justify-content: center;
    gap: 28px;
    font-size: 29px;
  }
  .rule {
    position: absolute;
    top: 941px;
    left: 98px;
    width: 603px;
    height: 4px;
    background: var(--ink);
  }
  .details {
    position: absolute;
    top: 960px;
    left: 98px;
    width: 605px;
    display: flex;
    justify-content: space-between;
    font-size: 40px;
  }
  .enquiries {
    position: absolute;
    left: 42px;
    top: 1090px;
    font-size: 29px;
    line-height: 32px;
  }
  .brand-mark {
    position: absolute;
    right: 40px;
    bottom: 60px;
    display: flex;
    align-items: center;
    gap: 10px;
    font-size: 34px;
  }
  .brand-mark svg { display: block; }
</style>
</head>
<body>
<main class="poster">
  <div class="backdrop" role="img" aria-label="Abstract background of glowing purple and blue fractal light swirls"></div>

  <header class="presenter">
    <p class="presenter-name">Lumora Entertainment</p>
    <p class="presenter-verb">present</p>
  </header>

  <p class="event-date">05.07.2014</p>

  <section class="lineup">
    <p class="lineup-row"><span>Bazzo (Akl)</span><span>DJ Glimtrax</span></p>
    <p class="lineup-row"><span>DJ's Morquent &amp; Pelnavo</span><span>Quiet Harbour Pulse</span></p>
  </section>

  <h1 class="party-name">TBD</h1>

  <p class="venue"><span>Dorrin Hattles Central</span><span>Corner Fenwick &amp; Oberly Streets</span></p>
  <div class="rule"></div>
  <p class="details"><span>10pm-close</span><span>R18</span><span>$10 Tickets</span></p>

  <p class="enquiries">Tickets &amp; Enquiries:<br>Marta on 0219047362</p>

  <div class="brand-mark">
    <svg width="22" height="22" viewBox="0 0 22 22" aria-hidden="true"><rect x="1" y="1" width="20" height="20" fill="none" stroke="#ffffff" stroke-width="2"/></svg>
    <span>Lumora</span>
  </div>
</main>
</body>
</html>
```